Business Card Design

An energy company designed around renewable energy and energy storage that focuses on providing its energy at points on the grid that reduce costs and add value to the system.

Industry/Entity Type

Business

Contact Information for Business Card

Martin Dellacroix
Executive Vice President
41 K ST NE
Washington, DC 20017
240-555-0187
mdellacroix@brightvaleenergy.example

```html
<!DOCTYPE html>
<html lang="en">
<head>
<meta charset="utf-8">
<title>Martin Dellacroix – Business Card</title>
<link href="https://fonts.googleapis.com/css2?family=Poiret+One&family=Source+Sans+3:wght@400;600&display=swap" rel="stylesheet">
<style>
  :root {
    --page-bg: #e6ebec;
    --card-bg: #323a3e;
    --name-light: #ffffff;
    --detail-grey: #8b9497;
    --rule-white: #e9ecec;
  }
  * { box-sizing: border-box; margin: 0; padding: 0; }
  html, body {
    width: 1200px;
    height: 1000px;
    overflow: hidden;
    background: var(--page-bg);
  }
  .card {
    position: absolute;
    left: 160px;
    top: 212px;
    width: 880px;
    height: 576px;
    background: var(--card-bg);
  }
  .identity {
    position: absolute;
    left: 0;
    right: 0;
    top: 190px;
    display: flex;
    justify-content: center;
  }
  .identity-block {
    display: inline-flex;
    flex-direction: column;
    align-items: flex-end;
  }
  .full-name {
    font-family: "Poiret One", sans-serif;
    font-weight: 400;
    font-size: 72px;
    line-height: 1;
    letter-spacing: 0;
    white-space: nowrap;
    color: var(--name-light);
  }
  .job-title {
    font-family: "Source Sans 3", sans-serif;
    font-weight: 400;
    font-size: 19px;
    color: var(--detail-grey);
    margin-top: 4px;
    margin-right: 4px;
  }
  .divider {
    position: absolute;
    top: 389px;
    height: 2px;
    background: var(--rule-white);
  }
  .divider-left { left: 37px; width: 211px; }
  .divider-right { left: 630px; width: 212px; }
  .divider-dot {
    position: absolute;
    top: -8px;
    width: 18px;
    height: 18px;
    border-radius: 50%;
    background: var(--rule-white);
  }
  .divider-left .divider-dot { left: 96px; }
  .divider-right .divider-dot { left: 95px; }
  .contact {
    position: absolute;
    left: 0;
    right: 0;
    top: 410px;
    text-align: center;
    font-family: "Source Sans 3", sans-serif;
    font-style: normal;
    font-weight: 400;
    font-size: 19px;
    line-height: 31px;
    color: var(--detail-grey);
  }
</style>
</head>
<body>
  <section class="card">
    <div class="identity">
      <div class="identity-block">
        <h1 class="full-name">MARTIN DELLACROIX</h1>
        <p class="job-title">Executive Vice President</p>
      </div>
    </div>
    <div class="divider divider-left"><span class="divider-dot"></span></div>
    <div class="divider divider-right"><span class="divider-dot"></span></div>
    <address class="contact">
      <p>41 K ST NE Washington, DC 20017 240-555-0187</p>
      <p>mdellacroix@brightvaleenergy.example</p>
    </address>
  </section>
</body>
</html>
```